Flyer for a Business Consultant

I need a one-page description of services. I am a Brennick Certifed Talents Mentor. I do not have a personal website but think I will soon purchase this template https://varlowskins.example/skins/lectern/. I like the larger font, simplicity and larger font. I will attach his pricing flyer which I like - not to overly guide or restrict your creative thinking, but only to give a little perspective. I don't like busy, noisy - I like clarity, simplicity. Here 's the Brennick website which these same traits https://www.brennicktalentshub.example/ and can be a source of ideas and colors.

Target Market(s)

CEOs and Middle Managers in organizations

Industry/Entity Type

Financial Service

Colors

Designer to choose colors to be used in the design.

Requirements
Must have
• Clarity, simplicity, but also strength (not weak or frilly looking)
Nice to have
• Warm color(s), larger/not skinny font
Should not have
• Loud, noisy, busy

```html
<!DOCTYPE html>
<html lang="en">
<head>
<meta charset="utf-8">
<title>Strength-Based Team Effectiveness Flyer</title>
<link rel="stylesheet" href="https://fonts.googleapis.com/css2?family=Bebas+Neue&family=Roboto+Condensed:wght@300;400;700&family=Roboto:wght@500&display=swap">
<style>
  :root {
    --stage: #1b1b1d;
    --paper: #ffffff;
    --band-grey: #8a8a8c;
    --soft-grey: #b7b7b9;
    --light-grey: #c9c9cb;
    --heading-grey: #8c8c8e;
    --ink: #2a2a2c;
    --dark-bar: #2d2a33;
    --check: #8f8f91;
  }
  * { box-sizing: border-box; margin: 0; padding: 0; }
  html, body { width: 1200px; height: 1200px; overflow: hidden; background: var(--stage); }
  .canvas { position: relative; width: 1200px; height: 1200px; }
  .flyer {
    position: absolute; left: 159px; top: 30px;
    width: 933px; height: 1206px;
    background: var(--paper);
    transform: scale(0.945); transform-origin: 0 0;
    overflow: hidden;
    font-family: "Roboto Condensed", sans-serif;
    color: var(--ink);
  }
  .abs { position: absolute; }

  .shelf-strip { left: 0; top: 0; width: 469px; height: 55px;
    background: linear-gradient(90deg, #6e2a1c, #a2553a 30%, #7a3a26 55%, #b46a45 80%, #5e2418); }
  .title-band { left: 0; top: 55px; width: 469px; height: 141px; background: var(--band-grey);
    padding: 30px 0 0 40px; }
  .title-band h1 { font-family: "Bebas Neue", sans-serif; font-weight: 400; color: #fff;
    font-size: 40px; line-height: 43px; letter-spacing: -0.2px; white-space: nowrap; text-transform: uppercase; }
  .rope-photo { left: 470px; top: 55px; width: 463px; height: 141px;
    background: linear-gradient(100deg, #3a2a1e 0%, #6b4a34 35%, #8a6148 55%, #3b2c22 80%, #1f1813 100%); }
  .portrait-photo { left: 0; top: 196px; width: 469px; height: 802px;
    background: linear-gradient(180deg, #9a4a3c 0%, #6a3a30 40%, #3a2c2c 65%, #23232c 100%);
    clip-path: polygon(0 0, 100% 0, 100% 86.3%, 26.6% 100%, 0 100%); }

  .services { left: 502px; top: 218px; width: 410px; }
  .services h2 { font-family: "Bebas Neue", sans-serif; font-weight: 400; color: var(--heading-grey);
    font-size: 34px; line-height: 38px; white-space: nowrap; text-transform: uppercase; letter-spacing: -0.2px; }
  .benefits { list-style: none; margin-top: 14px; width: 405px; }
  .benefits li { position: relative; padding-left: 21px; font-size: 17px; line-height: 22px; margin-bottom: 10px; }
  .benefits svg { position: absolute; left: 0; top: 5px; width: 14px; height: 12px; }
  .offer h2 { margin-top: 22px; margin-bottom: 8px; }
  .offer p { font-size: 15.5px; line-height: 20px; width: 388px; }

  .side-band { left: 0; top: 998px; width: 66px; height: 208px; background: var(--soft-grey); }
  .credential { left: 92px; top: 1000px; display: flex; align-items: center; gap: 14px; }
  .credential .mark { width: 48px; height: 48px; background: var(--band-grey); }
  .credential .label { font-weight: 400; color: #6d6d70; font-size: 15px; line-height: 20px; }
  .coach { left: 89px; top: 1074px; }
  .coach .name { font-weight: 400; font-size: 46px; line-height: 48px; color: #8a8a8c; }
  .coach .role { font-weight: 400; font-size: 20px; line-height: 26px; color: #8a8a8c; }

  .contact-top { left: 483px; top: 998px; width: 450px; height: 12px; background: var(--light-grey); }
  .contact-lines { left: 483px; top: 1014px; width: 450px; height: 38px;
    background: repeating-linear-gradient(180deg, var(--light-grey) 0 2px, #fff 2px 6px); }
  .contact-box { left: 483px; top: 1052px; width: 450px; height: 110px; background: var(--soft-grey);
    padding: 25px 0 0 21px; }
  .contact-box .email { font-size: 28px; line-height: 34px; color: #222; }
  .contact-box .phone { font-family: "Roboto", sans-serif; font-weight: 500; font-size: 27px; letter-spacing: 4px; color: #222; margin-top: 4px; }
  .dark-bar { left: 0; top: 1162px; width: 933px; height: 18px; background: var(--dark-bar); }
  .foot-right { left: 483px; top: 1180px; width: 450px; height: 26px; background: var(--soft-grey); }
</style>
</head>
<body>
<div class="canvas">
  <article class="flyer">
    <div class="abs shelf-strip" role="img" aria-label="Photo of bookshelf spines"></div>
    <header class="abs title-band">
      <h1>A Strength-Based Approach to<br>Managing Team Effectiveness</h1>
    </header>
    <div class="abs rope-photo" role="img" aria-label="Photo of hands in suit sleeves pulling a rope"></div>
    <div class="abs portrait-photo" role="img" aria-label="Portrait photo of the coach in a suit before a bookcase"></div>

    <section class="abs services">
      <h2>We Help Teams Grow Stronger By:</h2>
      <ul class="benefits">
        <li><svg viewBox="0 0 14 12"><path d="M1 6.5 L5 10 L13 1.5" fill="none" stroke="var(--check)" stroke-width="2.4"/></svg>Bringing a deep awareness of their strengths and the strengths of their associates.</li>
        <li><svg viewBox="0 0 14 12"><path d="M1 6.5 L5 10 L13 1.5" fill="none" stroke="var(--check)" stroke-width="2.4"/></svg>Increasing the Team’s communication and sense of partnership.</li>
        <li><svg viewBox="0 0 14 12"><path d="M1 6.5 L5 10 L13 1.5" fill="none" stroke="var(--check)" stroke-width="2.4"/></svg>Improving employee engagement and effectiveness.</li>
      </ul>
      <div class="offer">
        <h2>Individual Sessions</h2>
        <p>Conversational feedback and coaching sessions based on Brennick’s TalentPoint assessments. These sessions last about an hour and lead to a personalized translation of the results and how their strengths show up in their work and inherent blind spots they bring.</p>
      </div>
      <div class="offer">
        <h2>Strength Discovery Workshop</h2>
        <p>A retreat-style Team Workshop in which the team learns each other’s unique Top 5 strengths. The session is very interactive and provides a common language that leads to improved communication and effectiveness. Tailored in 2.3.and 4-hour options are tailored to your Team’s challenges and opportunities.</p>
      </div>
      <div class="offer">
        <h2>Follow-On Modules</h2>
        <p>Follow-on is important to make the insights learned to be practical and integrated into the Teams’ approach and workflows.<br>In a debrief session included as part of the workshop, we provide several 15-minute exercise modules for use in regular meetings, and we offer guest facilitated modules of 30- 60 minutes each.</p>
      </div>
    </section>

    <div class="abs side-band"></div>
    <div class="abs credential">
      <div class="mark"></div>
      <div class="label">BRENNICK CERTIFIED<br>Talents Mentor</div>
    </div>
    <div class="abs coach">
      <div class="name">Warren Ashcombe</div>
      <div class="role">Brennick Workplace Talents Mentor</div>
    </div>

    <div class="abs contact-top"></div>
    <div class="abs contact-lines"></div>
    <div class="abs contact-box">
      <div class="email">warren@talentsmetric.example</div>
      <div class="phone">555-014-2290</div>
    </div>
    <div class="abs dark-bar"></div>
    <div class="abs foot-right"></div>
  </article>
</div>
</body>
</html>
```